Website Redesign for Mortgage, Property and Conveyancing business

Project Overview:
We are looking for a refresh and redesign of our current website to a smart, crisp and fresh approach to Home Loans, Conveyancing and Property sales. This task will be to:
- Redesign our current website in accordance with the new wireframe.
- Provide all elements required for the design
- Build 7 key templates including:
Home Page
2nd Level Section Page
3rd level Product landing Page
2nd Level - About Us, Contact Us etc
Blog
Blog Article
Campaign Page - no header
Technical
The design is for a Wordpress website. Existing theme is Fenwickly and we use Elementor for page editing. We are open to a new theme to be introduced but would prefer to stay with elementor.
Current Site is: www.brondacove.com.au
Sites that we like or elements of sites:
Marlow Real Estate: https://www.marlow.com.au/ (Like use of video and navigation)
Quiet Harbour Lane - Mortage: https://qhl.com.au/refinance-home-loan/ (Like landing pages a sin example)
Pelvana: https://pelvana.com.au/ (like Our services section).
Industry/Entity Type
Mortgage, Property, Conveyancing, Property Investment
Coding
Coded - Design and coding required
Number of Pages Required
5+ page
Requirements
Must have
- Built for Wordpress and Elementor.
Nice to have
- See Project Description for links to ideas/elements that we have liked. However, open to ideas as long as the follow the navigation set out in the wire frame.

```html
<!DOCTYPE html>
<html lang="en">
<head>
<meta charset="utf-8">
<title>Brondacove Home Page Design</title>
<link href="https://fonts.googleapis.com/css2?family=Plus+Jakarta+Sans:wght@400;500;600;700;800&display=swap" rel="stylesheet">
<style>
:root{
  --green:#16a94a;
  --green-soft:#5acf6c;
  --mint:#cdeed0;
  --navy:#0b1257;
  --blue:#133f97;
  --mist:#e6eaf3;
  --card:#f3f3f3;
  --ink:#111111;
  --footer:#1b1b1b;
  --white:#ffffff;
  --star:#f5a623;
}
*{box-sizing:border-box;margin:0;padding:0}
html,body{width:1200px;height:1200px;overflow:hidden;background:var(--white)}
body{font-family:"Plus Jakarta Sans",Arial,sans-serif;color:var(--ink)}
.stage{position:relative;width:1200px;height:1200px;overflow:hidden}
.board{position:absolute;left:0;top:0;width:1920px;height:1920px;transform:scale(.625);transform-origin:0 0}
.abs{position:absolute}
.btn{position:absolute;display:flex;align-items:center;justify-content:center;background:var(--green);color:var(--white);font-weight:700;font-size:14px}
.sheet-title{left:0;width:1190px;top:132px;font-size:35px;font-weight:800;text-align:center}
.note{left:41px;top:283px;font-size:13px}
.brand{display:flex;align-items:center;gap:5px;font-size:17px;font-weight:500;color:var(--ink)}
.brand .mark{width:18px;height:18px;background:var(--blue)}
.nav-item{position:absolute;top:290px;font-size:8px;color:#666;white-space:nowrap}
.nav-item.on{color:var(--green);font-weight:700}
.hero{left:234px;top:316px;width:690px;height:308px;background:linear-gradient(120deg,#d9d6d1 0%,#c9b8a6 40%,#8a7a66 60%,#e2dfdb 100%)}
.hero-box{left:337px;top:376px;width:250px;height:150px;background:rgba(255,255,255,.35)}
.hero-title{left:350px;top:382px;width:240px;font-size:24px;line-height:29px;font-weight:700}
.hero-sub{left:350px;top:448px;font-size:12px;line-height:15px;width:190px}
.band{position:absolute}
.band-title{position:absolute;font-size:15px;font-weight:600;text-align:center}
.svc{position:absolute;top:726px;width:154px;height:104px;background:var(--white);text-align:center;padding-top:12px;font-size:11.5px;line-height:15px}
.svc b{display:block;font-weight:600;margin:8px 0 4px;font-size:12px}
.svc.hl{background:var(--green)}
.why{position:absolute;background:var(--card);padding:10px 8px}
.why.hl{background:var(--green)}
.why h3{font-size:11.5px;font-weight:700;line-height:14px;margin:14px 0 6px}
.why p{font-size:7.5px;line-height:13px;color:#333}
.why.hl p{color:#10301b}
.input{position:absolute;top:1486px;height:32px;background:var(--white);border:1px solid #bbb;font-size:8px;color:#888;padding:12px 8px}
.tm{position:absolute;width:112px;height:123px;background:var(--white);text-align:center}
.tm.hl{background:var(--green)}
.tm .av{width:60px;height:60px;border-radius:50%;background:linear-gradient(#c9ccd2,#5a5f6a);margin:14px auto 10px;border:2px solid var(--white)}
.tm b{display:block;font-size:12px;font-weight:700}
.tm span{font-size:8px}
.post{position:absolute;overflow:hidden;border-radius:8px;color:var(--white)}
.post .cat{position:absolute;font-size:7px;opacity:.85}
.post .t{position:absolute;font-size:9.5px;line-height:13px;font-weight:500}
.post .more{position:absolute;font-size:7px;border:1px solid rgba(255,255,255,.6);border-radius:10px;padding:2px 6px}
.rv{position:absolute;top:828px;width:154px;background:var(--card);padding:8px 10px;font-size:7.5px;line-height:13px;color:#333}
.rv.hl{background:var(--green);color:#0e2a17}
.rv b{display:block;font-size:12px;font-weight:600;color:var(--ink);margin-bottom:4px}
.rv .stars{color:var(--star);font-size:11px;letter-spacing:4px;margin-bottom:6px}
.info{position:absolute;top:1262px;height:108px;width:158px;padding:12px;font-size:8px;color:#555;line-height:17px}
.info h4{font-size:12px;color:var(--ink);margin:10px 0 4px;font-weight:700}
.foot-links{display:flex;gap:15px;font-size:8px;color:#ddd}
</style>
</head>
<body>
<div class="stage">
<div class="board">
  <div class="abs sheet-title">Brondacove Construction Company(Home page)</div>

  <div class="abs note">Video background</div>
  <svg class="abs" style="left:96px;top:312px" width="140" height="120" viewBox="0 0 140 120" fill="none" stroke="#111" stroke-width="1.6">
    <path d="M8 4 C14 50 60 90 128 110"/><path d="M118 100 L128 110 L116 116"/>
  </svg>

  <div class="abs brand" style="left:342px;top:284px"><span class="mark"></span>Brondacove</div>
  <span class="nav-item on" style="left:472px">Home</span>
  <span class="nav-item" style="left:511px">Finance</span>
  <span class="nav-item" style="left:554px">Property</span>
  <span class="nav-item" style="left:600px">Conveyancing</span>
  <span class="nav-item" style="left:666px">Blog</span>
  <span class="nav-item" style="left:697px">About Us</span>
  <div class="btn" style="left:745px;top:282px;width:78px;height:24px;font-size:9px;font-weight:500">Get a Quote</div>

  <div class="abs hero" role="img" aria-label="Looping video of a couple reviewing home plans with a small model house"></div>
  <div class="abs hero-box"></div>
  <div class="abs hero-title">Finance, Property, Conveyancing</div>
  <div class="abs hero-sub">Unlocking Opportunities and solving problems.</div>
  <div class="btn" style="left:350px;top:502px;width:96px;height:33px;font-size:12px">Lets talk</div>

  <div class="band" style="left:234px;top:624px;width:690px;height:237px;background:var(--navy)"></div>
  <div class="band-title" style="left:234px;width:690px;top:683px;color:var(--white)">SERVICES:</div>
  <div class="svc hl" style="left:335px">
    <svg width="22" height="22" viewBox="0 0 24 24" fill="none" stroke="#111" stroke-width="1.5"><path d="M3 9 L12 4 L21 9 Z M5 10v8 M9 10v8 M15 10v8 M19 10v8 M3 20h18"/></svg>
    <b>FINANCE</b>for your home, car, investments, and assets</div>
  <div class="svc" style="left:502px">
    <svg width="22" height="22" viewBox="0 0 24 24" fill="none" stroke="#111" stroke-width="1.5"><circle cx="10" cy="10" r="7"/><path d="M15 15 L21 21 M7 11 L10 8 L13 11 V13 H7 Z"/></svg>
    <b>PROPERTY</b>sales, purchases, and rentals</div>
  <div class="svc" style="left:670px">
    <svg width="22" height="22" viewBox="0 0 24 24" fill="none" stroke="#111" stroke-width="1.5"><rect x="4" y="8" width="12" height="13" rx="1"/><path d="M7 8 V5 a3 3 0 0 1 6 0 V8"/><circle cx="18" cy="17" r="3"/></svg>
    <b>CONVEYANCING</b>for seamless property transactions</div>

  <div class="band-title" style="left:234px;width:694px;top:920px">WHY BRONDACOVE</div>
  <div class="why hl" style="left:335px;top:970px;width:153px;height:142px">
    <svg width="26" height="24" viewBox="0 0 26 24" fill="none" stroke="#111" stroke-width="1.4"><rect x="2" y="4" width="22" height="18" rx="2"/><path d="M2 9h22 M7 2v4 M19 2v4"/><text x="7" y="19" font-size="8" fill="#111" stroke="none">20</text></svg>
    <h3>20 years experience</h3><p>We have grown and changed with the industry, and we're dedicated to continually improve our service and products so you get the best solutions possible.</p></div>
  <div class="why" style="left:502px;top:970px;width:154px;height:142px">
    <svg width="30" height="26" viewBox="0 0 30 26" fill="none" stroke="#111" stroke-width="1.2"><circle cx="7" cy="4" r="3"/><path d="M3 25 V12 h8 V25 M16 14 L22 9 L28 14 V24 H16 Z"/></svg>
    <h3>We give you choice</h3><p>Working with over 20 large and small lenders, property developers and switched on accountants, we have the scope to give you good choices for the future.</p></div>
  <div class="why" style="left:669px;top:970px;width:154px;height:142px">
    <svg width="30" height="26" viewBox="0 0 30 26" fill="none" stroke="#111" stroke-width="1.2"><circle cx="9" cy="14" r="3"/><path d="M4 25 a5 5 0 0 1 10 0 M20 2 h8 v12 h-8 Z M23 6 v5"/></svg>
    <h3>It is about the outcome</h3><p>When we say we care, we mean it. If you are a client now, we want you to be a happy client. If we cannot help you become a client today we'd like to help you tomorrow.</p></div>
  <div class="why" style="left:335px;top:1121px;width:153px;height:156px">
    <svg width="24" height="30" viewBox="0 0 24 30" fill="none" stroke="#111" stroke-width="1.2"><circle cx="12" cy="5" r="3"/><path d="M12 8 V18 M6 18 h12 v10 H6 Z"/></svg>
    <h3>We give you options that makes sense</h3><p>We have grown and changed with the industry, and we're dedicated to continually improve our service and products so you get the best solutions possible.</p></div>
  <div class="why" style="left:502px;top:1121px;width:321px;height:116px">
    <svg width="30" height="26" viewBox="0 0 30 26" fill="none" stroke="#111" stroke-width="1.2"><circle cx="7" cy="4" r="3"/><path d="M3 25 V12 h8 V25 M16 14 L22 9 L28 14 V24 H16 Z"/></svg>
    <h3>We give you choice</h3><p>Working with over 20 large and small lenders, property developers and switched on accountants, we have the scope to give you good choices for the future.</p></div>
  <div class="btn" style="left:524px;top:1301px;width:109px;height:33px;font-size:13px">View More</div>

  <div class="band" style="left:234px;top:1394px;width:690px;height:156px;background:var(--mint)"></div>
  <div class="band-title" style="left:234px;width:690px;top:1424px;line-height:20px;font-size:16px">SUBSCRIBE TO KEEP UP TO DATE ON<br>MARKET NEWS</div>
  <div class="input" style="left:336px;width:152px">Your name</div>
  <div class="input" style="left:502px;width:154px">Your Email</div>
  <div class="btn" style="left:670px;top:1486px;width:153px;height:32px;font-size:8px">Subscribe</div>

  <div class="band" style="left:234px;top:1550px;width:690px;height:282px;background:var(--blue)"></div>
  <div class="band-title" style="left:234px;width:690px;top:1579px;color:var(--white);font-size:16px;font-weight:500">Your dream Our team</div>
  <div class="tm hl" style="left:335px;top:1622px"><div class="av" role="img" aria-label="Team member portrait"></div><b>Owen Telford</b><span>General manager</span></div>
  <div class="tm" style="left:460px;top:1622px"><div class="av" role="img" aria-label="Team member portrait"></div><b>Owen Telford</b><span>General manager</span></div>
  <div class="tm" style="left:586px;top:1622px"><div class="av" role="img" aria-label="Team member portrait"></div><b>Owen Telford</b><span>General manager</span></div>
  <div class="tm" style="left:711px;top:1622px"><div class="av" role="img" aria-label="Team member portrait"></div><b>Owen Telford</b><span>General manager</span></div>
  <div class="btn" style="left:485px;top:1768px;width:187px;height:33px;font-size:12.5px">See More Team Member</div>

  <div class="band" style="left:234px;top:1832px;width:690px;height:100px;background:var(--mist)"></div>
  <div class="band-title" style="left:234px;width:690px;top:1892px;font-size:16px;font-weight:500">Blog and Insight</div>

  <div class="band" style="left:1037px;top:0;width:690px;height:273px;background:var(--blue)"></div>
  <div class="band-title" style="left:1037px;width:690px;top:20px;color:var(--white);font-size:16px;font-weight:500">Your dream Our team</div>
  <div class="tm hl" style="left:1138px;top:63px"><div class="av" role="img" aria-label="Team member portrait"></div><b>Owen Telford</b><span>General manager</span></div>
  <div class="tm" style="left:1264px;top:63px"><div class="av" role="img" aria-label="Team member portrait"></div><b>Owen Telford</b><span>General manager</span></div>
  <div class="tm" style="left:1389px;top:63px"><div class="av" role="img" aria-label="Team member portrait"></div><b>Owen Telford</b><span>General manager</span></div>
  <div class="tm" style="left:1515px;top:63px"><div class="av" role="img" aria-label="Team member portrait"></div><b>Owen Telford</b><span>General manager</span></div>
  <div class="btn" style="left:1287px;top:209px;width:189px;height:33px;font-size:12.5px">See More Team Member</div>

  <div class="band" style="left:1037px;top:273px;width:690px;height:453px;background:var(--mist)"></div>
  <div class="band-title" style="left:1037px;width:690px;top:333px;font-size:16px;font-weight:500">Blog and Insight</div>
  <div class="post" style="left:1145px;top:377px;width:189px;height:130px;background:linear-gradient(160deg,#e6b64a,#8a6a2a 70%,#3a2e1a)" role="img" aria-label="Blog photo of a woman in a knitted hat on a golden field">
    <span class="cat" style="left:11px;top:56px">BAD CREDIT, BLOG</span>
    <span class="t" style="left:11px;top:70px;width:165px">Credit Scores- What are they and how do they affect you</span>
    <span class="more" style="left:11px;top:105px">Learn More ↗</span></div>
  <div class="post" style="left:1143px;top:517px;width:189px;height:131px;background:linear-gradient(150deg,#6b8f3a,#3f5a24 60%,#26361a)" role="img" aria-label="Blog photo of a money bag and model house on grass">
    <span class="cat" style="left:10px;top:69px">CONSTRUCTION</span>
    <span class="t" style="left:10px;top:83px">Poor Credit home loan Refinance</span>
    <span class="more" style="left:12px;top:106px">Learn More ↗</span></div>
  <div class="post" style="left:1348px;top:377px;width:272px;height:271px;background:linear-gradient(135deg,#7aa3b8,#4a6d82 50%,#2c3e4c)" role="img" aria-label="Blog photo of a team reviewing architectural models">
    <span class="cat" style="left:11px;top:209px">CONSTRUCTION</span>
    <span class="t" style="left:11px;top:223px">Understanding Appraisals</span>
    <span class="more" style="left:13px;top:246px">Learn More ↗</span></div>
  <div class="btn" style="left:1328px;top:672px;width:104px;height:23px;font-size:9px;background:var(--green-soft);color:var(--ink);font-weight:600">Read All Blogs ▯</div>

  <div class="band-title" style="left:1037px;width:690px;top:785px;font-size:16px;font-weight:600">Read what our clients say About us</div>
  <div class="rv" style="left:1138px"><b>Dane</b><div class="stars">★★★★★</div>2nd time to utilise Tess for Conveyancing. Tess has once again made transactions regarding property a breeze. Any questions you may have, she will answer them with the best of her ability and reassure you that you are in good hands!</div>
  <div class="rv hl" style="left:1305px"><b>Mira and Joel</b><div class="stars">★★★★★</div>customer service achieving exactly what we were after, quickly and efficiently. Paul Varga kept us updated regularly throughout the process, making the whole process seamless and easy. Everything was explained to us throughout without any unexpected surprises.</div>
  <div class="rv" style="left:1472px"><b>Ivo Mc</b><div class="stars">★★★★★</div>Perfect Service Thoroughly Recommended. Conveyancing contract execution was so easy with Brondacove, our back-to-back agreements come together without any issues. Highly recommend without reservation.</div>
  <svg class="abs" style="left:1129px;top:895px" width="16" height="16" viewBox="0 0 16 16"><circle cx="8" cy="8" r="8" fill="#ddd"/><path d="M9.5 4.5 L6 8 L9.5 11.5" stroke="#333" fill="none" stroke-width="1.3"/></svg>
  <svg class="abs" style="left:1618px;top:895px" width="16" height="16" viewBox="0 0 16 16"><circle cx="8" cy="8" r="8" fill="#16a94a"/><path d="M6.5 4.5 L10 8 L6.5 11.5" stroke="#111" fill="none" stroke-width="1.3"/></svg>
  <svg class="abs" style="left:1366px;top:1021px" width="32" height="8"><circle cx="4" cy="4" r="2.5" fill="#ccc"/><circle cx="16" cy="4" r="2.5" fill="#16a94a"/><circle cx="28" cy="4" r="2.5" fill="#ccc"/></svg>

  <div class="band" style="left:1037px;top:1087px;width:690px;height:329px;background:linear-gradient(180deg,#7fb9d6 0%,#b9d6e4 35%,#d9cbb8 70%,#c8b49a 100%)" role="img" aria-label="Photo of a smiling family of four at the beach"></div>
  <div class="info" style="left:1145px;background:#f5f5f5">
    <svg width="24" height="24" viewBox="0 0 24 24" fill="none" stroke="#111" stroke-width="1.4"><circle cx="12" cy="12" r="10"/><path d="M12 6 V12 L16 14"/></svg>
    <h4>Opening Times</h4>Monday – Friday: 9am–5pm<br>Saturday – Sunday: Closed</div>
  <div class="info" style="left:1303px;background:var(--green-soft);color:#0f2c17">
    <svg width="24" height="24" viewBox="0 0 24 24" fill="none" stroke="#111" stroke-width="1.4"><path d="M5 3 h4 l2 5 -3 2 a11 11 0 0 0 6 6 l2 -3 5 2 v4 a2 2 0 0 1 -2 2 A17 17 0 0 1 3 5 a2 2 0 0 1 2 -2 Z"/></svg>
    <h4>Contact Us</h4>info@brondacove.com.au<br>1300 555 014</div>
  <div class="info" style="left:1461px;width:159px;background:#f5f5f5;line-height:10px">
    <svg width="24" height="24" viewBox="0 0 24 24" fill="none" stroke="#111" stroke-width="1.4"><path d="M12 22 C6 15 5 12 5 9 a7 7 0 0 1 14 0 c0 3 -1 6 -7 13 Z"/><circle cx="12" cy="9" r="2.5"/></svg>
    <h4 style="margin-top:6px">Reach Us</h4><div style="margin-top:8px">14 Tallow Street, Kelby Hill, VIC 3170</div>
    <svg style="margin-top:8px" width="46" height="10" viewBox="0 0 46 10" fill="none" stroke="#333" stroke-width="1"><rect x="1" y="1" width="8" height="8" rx="1.5"/><circle cx="21" cy="5" r="4"/><rect x="33" y="1.5" width="10" height="7" rx="2"/></svg></div>

  <div class="band" style="left:1037px;top:1416px;width:690px;height:196px;background:var(--footer)"></div>
  <div class="abs brand" style="left:1327px;top:1460px;color:var(--white);font-size:20px"><span class="mark" style="width:22px;height:22px;background:var(--white)"></span>Brondacove</div>
  <div class="abs foot-links" style="left:1245px;top:1506px"><span>Home</span><span>Finance</span><span>Property</span><span>Conveyancing</span><span>Blog</span><span>About Us</span></div>
  <div class="abs" style="left:1145px;top:1548px;width:475px;height:1px;background:#666"></div>
  <div class="abs" style="left:1145px;top:1564px;font-size:6.5px;color:#ccc">© 2023 Brondacove. All rights reserved.</div>
  <div class="abs" style="left:1455px;top:1564px;font-size:6.5px;color:#ccc;display:flex;gap:12px;text-decoration:underline"><span>Privacy Policy</span><span>Terms of Service</span><span>Cookies Settings</span></div>
</div>
</div>
</body>
</html>
```